Custom Framing Shop Tallpine Framing Studio

I want an eye catching graphic that will be used a s business sign on a busy road. The sign MUST communicate the type of business it is clearly to vehicles traveling at 40 mph. This is a custom picture framing business and the sign will be hanging and be approximately 32" X 48". The business name is Tallpine Framing Studio; Custom framing: by appointment and should include a whole or partial image of a picture frame as a visual que. I've included inspiration idea's, color pallets and styles that I like and a current business card for inspiration. I like the crimson font style shadowing and background colors of the attached Olans pizzeria sign. I'd prefer crimson letters. Custom Framing is the message to communicate, followed by phone number and business name. I like the idea of a shield shape with a banner since it would more eye catching, Once again the Tallpine image and name is less important than communicating what the business does. I like Crimson, grey, gold, black but am open to new ideas . I like the idea of a shield with a banner more than a rectangle, but am open to idea's

Target Market(s)

My target market is local homeowners ($700k+) who want a relationship with their framer and are willing to pay for a customized experience compared to a craft store experience. I have more female clients then men.

Industry/Entity Type

Picture Framing Art

Other font styles liked:
• Look at the attached image of a custom pizzeria sign, its kid of a custom car pinstripe font style. Script and decorative may be difficult to read while driving by but add to the elegance.

Colors

Designer to choose colors to be used in the design.

Requirements
Must have
• Clearly communicate what the business does "Custom framing" preferably with a picture frame and words
Nice to have
• incorporate a Tallpine into the graphic
Should not have
• A Tallpine image doesn't communicate what the business does to a vehicle traveling at 40 mph by the sign

```html
<!DOCTYPE html>
<html lang="en">
<head>
<meta charset="utf-8">
<title>Tallpine Framing Studio – Hanging Sign</title>
<link rel="stylesheet" href="https://fonts.googleapis.com/css2?family=Cinzel:wght@700;900&family=Montserrat:wght@800&family=Oswald:wght@600&display=swap">
<style>
  :root {
    --crimson: #7a1418;
    --crimson-dark: #5e0e12;
    --gold: #d9b45a;
    --gold-light: #efd98f;
    --cream: #f7edd6;
    --cream-light: #fbf5e4;
    --beige: #e9dcc0;
    --taupe: #cfc196;
    --ink: #111111;
    --white: #ffffff;
    --page: #ffffff;
  }
  html, body {
    margin: 0;
    padding: 0;
    width: 882px;
    height: 1200px;
    overflow: hidden;
    background: var(--page);
  }
  .sign {
    position: absolute;
    left: 31px;
    top: 326px;
    width: 820px;
    height: 549px;
    filter: drop-shadow(0 6px 10px rgba(0,0,0,0.18));
  }
  .sign__custom {
    font-family: "Cinzel", "Times New Roman", serif;
    font-weight: 700;
    fill: var(--crimson);
  }
  .sign__framing {
    font-family: "Cinzel", "Times New Roman", serif;
    font-weight: 900;
    fill: var(--white);
  }
  .sign__phone {
    font-family: "Montserrat", Arial, sans-serif;
    font-weight: 800;
    fill: var(--white);
  }
  .brand__name {
    font-family: "Oswald", Arial, sans-serif;
    font-weight: 600;
    fill: var(--ink);
  }
</style>
</head>
<body>
<svg class="sign" viewBox="0 0 1210 810" xmlns="http://www.w3.org/2000/svg" aria-label="Custom Framing sign for Tallpine Framing Studio">
  <defs>
    <path id="sign-shape" d="M380,0 H830 Q905,0 910,70 H1140 V115 H1165 C1165,260 1210,300 1210,420 C1210,540 1165,580 1165,720 H1140 V740 H910 Q905,810 830,810 H380 Q305,810 300,740 H70 V720 H45 C45,580 0,540 0,420 C0,300 45,260 45,115 H70 V70 H300 Q305,0 380,0 Z"/>
    <linearGradient id="gold-edge" x1="0" y1="0" x2="1" y2="1">
      <stop offset="0" stop-color="var(--gold-light)"/>
      <stop offset="0.5" stop-color="var(--gold)"/>
      <stop offset="1" stop-color="#b8862e"/>
    </linearGradient>
    <linearGradient id="cream-face" x1="0" y1="0" x2="0" y2="1">
      <stop offset="0" stop-color="var(--cream-light)"/>
      <stop offset="1" stop-color="var(--cream)"/>
    </linearGradient>
  </defs>

  <!-- layered border -->
  <use href="#sign-shape" fill="url(#gold-edge)"/>
  <use href="#sign-shape" fill="var(--crimson)" transform="translate(605 405) scale(0.978) translate(-605 -405)"/>
  <use href="#sign-shape" fill="var(--taupe)" transform="translate(605 405) scale(0.962) translate(-605 -405)"/>
  <use href="#sign-shape" fill="url(#cream-face)" transform="translate(605 405) scale(0.935) translate(-605 -405)"/>

  <!-- business name -->
  <g class="brand">
    <text class="brand__name" x="605" y="168" font-size="62" text-anchor="middle" letter-spacing="1">TALLPINE</text>
    <text class="brand__name" x="721" y="206" font-size="25" text-anchor="end" letter-spacing="1">Framing Studio</text>
  </g>

  <!-- picture frame -->
  <g class="frame">
    <rect x="175" y="280" width="860" height="300" fill="var(--beige)"/>
    <rect x="195" y="298" width="820" height="282" fill="var(--taupe)" opacity="0.45" role="img" aria-label="Ornamental carved picture-frame moulding"/>
    <rect x="235" y="338" width="740" height="242" fill="var(--crimson)"/>
    <rect x="247" y="350" width="716" height="230" fill="var(--cream)"/>
    <rect x="262" y="365" width="686" height="215" fill="var(--crimson)"/>
    <rect x="272" y="375" width="666" height="205" fill="var(--cream-light)"/>
  </g>

  <text class="sign__custom" x="605" y="510" font-size="118" text-anchor="middle">CUSTOM</text>

  <!-- banner and phone plate -->
  <rect x="110" y="530" width="990" height="125" fill="var(--crimson)"/>
  <path d="M310,655 H900 V700 Q895,770 830,770 H380 Q315,770 310,700 Z" fill="var(--crimson)"/>
  <text class="sign__framing" x="605" y="642" font-size="128" text-anchor="middle">FRAMING</text>
  <text class="sign__phone" x="605" y="728" font-size="56" text-anchor="middle">(555) 014-7290</text>
</svg>
</body>
</html>
```